Dental Design, very professional and noticable

Tindale Ridge Dental Surgery is based in Pelican Waters. We are a fast growing dental surgery and are looking for some professional business cards to send to patients.
We would like to see a design that is Vertical and uses the colours Soft Blue, Silver, White and Black. Maybe a full blue side with moto and details on back? Any other ideas or colours that you may think will make the card look unique is fine.
We need all details on the card that are listed above

Target Market(s)

Families, Retired, Other Professionals and Businesses

Industry/Entity Type

Dental

Contact Information for Business Card

Tindale Ridge Dental Surgery
Family, Cosmetic, Preventative
Dr. Owen Castrey
Dental Surgeon
BDS (Adel) FAE FADI FICD FPFA
phone: (07)50001846
fax: (07)50002917
email: tindaleridgedental@quillpost.com
http://tindaleridgedental.com/

Logo Text

Logo styles of interest
Abstract Logo
Requirements
Must have
• Vertical, Vibrant but Professional, Rounded Edges, Logo on front and back of card (different colours on each side)
Nice to have
• One side completely blue (not sure what shade) with logo and moto on bottom
Other side white, with blue or different coloured logo with details in black and silver?
Logo should show half circle with 1 end as arrow symbolizing pelican waters canal also a magnifine glass also half circled with 1 end as arrow. Any other ideas are welcome.
Should not have
• A tooth. A smile. Toothbrush or Toothpaste. Cornered edges.

```html
<!DOCTYPE html>
<html lang="en">
<head>
<meta charset="utf-8">
<title>Tindale Ridge Dental Surgery – Business Card</title>
<link rel="stylesheet" href="https://fonts.googleapis.com/css2?family=Arvo:wght@400;700&display=swap">
<style>
  :root {
    --card-blue: #74cff4;
    --ink: #0b0b0b;
    --paper: #ffffff;
  }
  html, body {
    margin: 0;
    padding: 0;
    width: 741px;
    height: 1200px;
    overflow: hidden;
    background: var(--card-blue);
  }
  .card {
    position: relative;
    width: 741px;
    height: 1200px;
    background: var(--card-blue);
    font-family: "Arvo", "Rockwell", serif;
    color: var(--ink);
  }
  .line {
    position: absolute;
    left: 0;
    right: 0;
    margin: 0;
    text-align: center;
    white-space: nowrap;
    line-height: 1;
  }
  .brand-mark {
    position: absolute;
    left: 0;
    right: 0;
    top: 190px;
    display: flex;
    flex-direction: column;
    align-items: center;
    gap: 18px;
  }
  .brand-mark__dot {
    width: 92px;
    height: 92px;
    border-radius: 50%;
    background: var(--paper);
  }
  .brand-mark__name {
    font-size: 40px;
    font-weight: 700;
    color: var(--ink);
    letter-spacing: 1px;
  }
  .practice-name { top: 384px; font-size: 52px; font-weight: 400; letter-spacing: -0.5px; color: var(--ink); }
  .practice-type { top: 436px; font-size: 52px; font-weight: 400; letter-spacing: -0.5px; color: var(--paper); }
  .motto { top: 486px; font-size: 27px; color: var(--ink); }
  .dentist-name { top: 594px; font-size: 41px; font-weight: 700; letter-spacing: 0.5px; }
  .dentist-role { top: 640px; font-size: 23px; }
  .dentist-credentials { top: 672px; font-size: 23px; }
  .contact-numbers { top: 733px; font-size: 25px; }
  .contact-email { top: 766px; font-size: 25px; }
  .label { color: var(--paper); }
  .email-user { color: var(--paper); font-weight: 700; }
  .address-street { top: 827px; font-size: 25px; }
  .address-town { top: 858px; font-size: 25px; }
  .website { top: 921px; font-size: 27px; font-weight: 700; color: var(--paper); }
  .social-prompt {
    top: 977px;
    font-size: 21px;
    color: var(--paper);
    display: flex;
    justify-content: center;
    align-items: center;
    gap: 8px;
    padding-left: 20px;
  }
  .social-prompt__square {
    width: 34px;
    height: 34px;
    border-radius: 7px;
    background: var(--paper);
  }
  .social-page { top: 1016px; font-size: 26px; color: var(--paper); }
</style>
</head>
<body>
  <main class="card">
    <div class="brand-mark">
      <span class="brand-mark__dot"></span>
      <span class="brand-mark__name">Tindale Ridge</span>
    </div>

    <h1 class="line practice-name">TINDALE RIDGE</h1>
    <p class="line practice-type">DENTAL SURGERY</p>
    <p class="line motto">Family, Cosmetic, Preventative</p>

    <h2 class="line dentist-name">DR. OWEN CASTREY</h2>
    <p class="line dentist-role">DENTAL SURGEON</p>
    <p class="line dentist-credentials">BDS (ADEL) FAE FADI FICD FPFA</p>

    <p class="line contact-numbers"><span class="label">P:</span> (07)50001846 <span class="label">F:</span> (07)50002917</p>
    <p class="line contact-email"><span class="email-user">tindaleridgedental</span>@quillpost.com</p>

    <p class="line address-street">Shop 7/18 Tindale Ridge Blvd</p>
    <p class="line address-town">Tindale Ridge, QLD, 4570</p>

    <p class="line website">www.tindaleridgedental.com</p>

    <p class="line social-prompt"><span class="social-prompt__square"></span><span>Like Us:</span></p>
    <p class="line social-page">Tindale Ridge Dental Surgery</p>
  </main>
</body>
</html>
```